Velmora Flowers Florist Flyer

We are requiring a flyer that advertises and promotes our new business. We specialise in weddings and events but would also like to branch out to corporates and an online subscription. Our brand is feminine/romantic with a touch of elegance and luxury. Our main colour schemes are white, black, gold and pale pink. Instagram: Velmora_flowers and website www.velmoraflowers.com.au
Target Market(s)
brides to be, females
Industry/Entity Type
Florist
Font styles to use
Sans Serif
Script
Other font styles liked:
- The Carpenter
Colors
ffffff
000000
333333
Requirements
Must have
- Feminine/romantic feel, through use of theme colours and elegant font
- our contact details Ph: 0478215096
- email address: contactus@velmoraflowers.com.au
Nice to have
- a description of us willing to work with clients to create their dream wedding flowers. That we offer consultations and no obligation quotes.

```html
<!DOCTYPE html>
<html lang="en">
<head>
<meta charset="utf-8">
<title>Velmora Flowers – Flyer</title>
<link href="https://fonts.googleapis.com/css2?family=Great+Vibes&family=Yellowtail&family=Alegreya:ital,wght@0,400;1,400;1,700&display=swap" rel="stylesheet">
<style>
  :root{
    --bg:#cfcfcf;
    --paper:#ffffff;
    --ink:#231f20;
    --header:#262626;
    --pink:#e9a9c9;
    --pink-soft:#f1c2d9;
    --gold:#c9a22f;
    --gold-dark:#8a6a12;
  }
  *{margin:0;padding:0;box-sizing:border-box}
  html,body{width:1200px;height:1200px;overflow:hidden;background:var(--bg)}
  .flyer{position:absolute;left:187px;top:21px;width:825px;height:1157px;background:var(--paper);overflow:hidden;font-family:"Alegreya",serif;color:var(--ink)}
  .masthead{position:absolute;left:0;top:0;width:825px;height:227px;background:var(--header);display:flex;align-items:center;justify-content:center}
  .brand-name{font-family:"Great Vibes",cursive;font-size:82px;color:#fff;font-weight:400;line-height:1}
  .pattern-band{position:absolute;left:0;top:227px;width:825px;height:32px;background:linear-gradient(90deg,#3a2a31,#5a3a48 50%,#3a2a31)}
  .pattern-band::after{content:"";position:absolute;left:0;right:0;top:13px;height:6px;background:var(--pink);opacity:.75}
  .venue-photo{position:absolute;left:0;top:258px;width:825px;height:480px;display:block}
  .title{position:absolute;left:0;width:825px;top:718px;text-align:center;font-family:"Yellowtail",cursive;font-size:76px;line-height:1;color:var(--ink)}
  .tagline{position:absolute;left:0;width:825px;top:798px;text-align:center;font-style:italic;font-size:19px;color:#333}
  .quote-frame{position:absolute;left:64px;top:854px;width:694px;height:78px;display:block}
  .quote{position:absolute;left:84px;top:862px;width:654px;text-align:center;font-style:italic;font-weight:700;font-size:22px;line-height:31px}
  .quote-author{position:absolute;left:617px;top:906px;font-size:13.5px;letter-spacing:.3px}
  .qmark{position:absolute;font-family:"Alegreya",serif;font-size:44px;color:var(--pink);line-height:1}
  .qmark.open{left:78px;top:846px}
  .qmark.close{left:742px;top:899px}
  .about-heading{position:absolute;left:50px;top:950px;font-style:italic;font-weight:700;font-size:20px}
  .about-col{position:absolute;top:979px;width:347px;font-style:italic;font-size:13.4px;line-height:17.5px;text-align:justify}
  .about-col.left{left:52px}
  .about-col.right{left:429px}
  .contact-bar{position:absolute;left:49px;top:1071px;width:727px;height:38px;border-radius:9px;background:var(--pink-soft);display:flex;align-items:center;padding:0 14px;gap:0;font-size:14px}
  .contact-item{display:flex;align-items:center;gap:8px;margin-right:27px}
  .contact-item svg{width:20px;height:20px;flex:none}
  .social{display:flex;gap:10px;margin-left:auto}
  .social span{width:18px;height:18px;border-radius:50%;background:var(--ink);display:block}
</style>
</head>
<body>
<main class="flyer">
  <header class="masthead">
    <h1 class="brand-name">Velmora Flowers</h1>
  </header>
  <div class="pattern-band" role="img" aria-label="Pink ornamental scroll border"></div>

  <svg class="venue-photo" viewBox="0 0 825 480" role="img" aria-label="Wedding reception hall with candlelit tables, a floral centrepiece and a tiered cake before windows onto green hills">
    <defs>
      <linearGradient id="photoTone" x1="0" y1="0" x2="0" y2="1">
        <stop offset="0" stop-color="#c8d3c4"/>
        <stop offset=".28" stop-color="#8da27a"/>
        <stop offset=".5" stop-color="#5b5740"/>
        <stop offset=".7" stop-color="#3a2a26"/>
        <stop offset="1" stop-color="#2a1e1c"/>
      </linearGradient>
      <radialGradient id="bloom" cx=".5" cy=".7" r=".35">
        <stop offset="0" stop-color="#efd9d2" stop-opacity=".7"/>
        <stop offset="1" stop-color="#efd9d2" stop-opacity="0"/>
      </radialGradient>
      <linearGradient id="goldLine" x1="0" x2="1">
        <stop offset="0" stop-color="#8a6a12"/>
        <stop offset=".5" stop-color="#f0d36a"/>
        <stop offset="1" stop-color="#8a6a12"/>
      </linearGradient>
    </defs>
    <path d="M0 0H825V430Q740 470 620 450Q520 430 412 410Q305 430 205 450Q85 470 0 430Z" fill="url(#photoTone)"/>
    <path d="M0 0H825V430Q740 470 620 450Q520 430 412 410Q305 430 205 450Q85 470 0 430Z" fill="url(#bloom)"/>
    <path d="M0 430Q85 470 205 450Q305 430 412 410Q520 430 620 450Q740 470 825 430" fill="none" stroke="url(#goldLine)" stroke-width="4"/>
  </svg>

  <h2 class="title">Velmora Flower</h2>
  <p class="tagline">Creating stunning Flowers for Weddings and Events</p>

  <svg class="quote-frame" viewBox="0 0 694 78" aria-hidden="true">
    <rect x="2" y="2" width="690" height="74" rx="37" fill="none" stroke="var(--gold)" stroke-width="2.5"/>
  </svg>
  <span class="qmark open">“</span>
  <p class="quote">Design is not making beauty, beauty emerges from selection, affinities, integration, love.</p>
  <span class="quote-author">- LORIN KADE</span>
  <span class="qmark close">”</span>

  <h3 class="about-heading">About Us:</h3>
  <p class="about-col left">For generations we've been creating flowers for family and friends. Over the years this has been our test bed for creating our design pieces for weddings and events. Now we want to make our beautiful creations available to everyone.</p>
  <p class="about-col right">Our designers have had extensive backgrounds, from owning a florist, to chocolate bouquet design and creations. Our friends and family loved working with our designers to create their perfect flower design, no matter what the event was</p>

  <footer class="contact-bar">
    <div class="contact-item">
      <svg viewBox="0 0 20 20" aria-hidden="true"><rect x="3.5" y="3.5" width="13" height="13" transform="rotate(45 10 10)" fill="#231f20"/><path d="M7.6 7c.4-.4.9-.3 1.1.1l.6 1.1c.2.4 0 .7-.3 1l-.3.3c.3.7.9 1.3 1.6 1.6l.3-.3c.3-.3.6-.5 1-.3l1.1.6c.4.2.5.7.1 1.1-.7.8-1.8.9-3.2.1-1.2-.7-2-1.6-2.5-2.7-.3-.9-.2-1.6.5-2z" fill="#fff"/></svg>
      <span>+61 4 782 150 96</span>
    </div>
    <div class="contact-item">
      <svg viewBox="0 0 20 20" aria-hidden="true"><rect x="3.5" y="3.5" width="13" height="13" transform="rotate(45 10 10)" fill="#231f20"/><rect x="6.8" y="7.8" width="6.4" height="4.4" fill="none" stroke="#fff" stroke-width="1"/><path d="M6.8 7.8L10 10.3 13.2 7.8" fill="none" stroke="#fff" stroke-width="1"/></svg>
      <span>contactus@velmoraflowers.com.au</span>
    </div>
    <div class="contact-item">
      <svg viewBox="0 0 20 20" aria-hidden="true"><rect x="3.5" y="3.5" width="13" height="13" transform="rotate(45 10 10)" fill="#231f20"/><circle cx="10" cy="10" r="3.3" fill="none" stroke="#fff" stroke-width="1"/><path d="M6.7 10h6.6M10 6.7c-1.4 2-1.4 4.6 0 6.6M10 6.7c1.4 2 1.4 4.6 0 6.6" fill="none" stroke="#fff" stroke-width=".8"/></svg>
      <span>www.velmoraflowers.com.au</span>
    </div>
    <div class="social" aria-label="Social media">
      <span></span><span></span><span></span>
    </div>
  </footer>
</main>
</body>
</html>
```